We need a 4-sided broschure design to present our new products.
The brochure will be send as a pdf file to our customers. So it should be landscape format. The name of the tif-files is the item number. It should be placed under the product shots. Similar products should be placed close together. Logo is attached. Claim - should be placed near the logo: Europe’s leading Afro-American Beauty Supplier
Contact dates: www.lumvarex.de | info@lumvarex.de | Tel +49 (0) 73 28 - 4 52 17 | Fax +49 (0) 73 28 - 45 21 93
Please download the product shots here: www.lumvarex.de/2015/brushtally/Newsletter_Februar.zip

```html
<!DOCTYPE html>
<html lang="en">
<head>
<meta charset="utf-8">
<title>Lumvarex of Beauty – Product Brochure</title>
<link rel="stylesheet" href="https://fonts.googleapis.com/css2?family=Noto+Serif:wght@400;700&family=Open+Sans:wght@400;600&display=swap">
<style>
  :root {
    --stage: #d5d5d5;
    --paper: #ffffff;
    --cover-paper: #f1f0ee;
    --pink: #e0328a;
    --ink: #555555;
    --ink-soft: #8a8a8a;
    --black: #1f1f1f;
    --band: #e9e9e9;
    --contact: #4d6c9c;
    --grey-box: #5c5c5c;
    --photo-skin: #6b4634;
    --photo-light: #e8e6e2;
    --photo-dress: #7d7c78;
    --fold: #e2e2e2;
  }
  * { box-sizing: border-box; margin: 0; padding: 0; }
  html, body { width: 1200px; height: 914px; overflow: hidden; }
  body {
    background: var(--stage);
    font-family: "Open Sans", Arial, sans-serif;
    color: var(--ink);
    position: relative;
  }
  .page {
    position: absolute;
    background: var(--paper);
    box-shadow: 0 2px 6px rgba(0,0,0,0.18);
    overflow: hidden;
  }

  /* Front cover */
  .front-cover { left: 40px; top: 50px; width: 520px; height: 368px; background: var(--cover-paper); }
  .cover-photo {
    position: absolute; right: 0; top: 0; width: 236px; height: 368px;
    background: linear-gradient(180deg, var(--photo-light) 0%, var(--photo-skin) 28%, var(--photo-skin) 46%, var(--photo-dress) 62%, #5e5d5a 100%);
  }
  .brand { display: flex; align-items: center; gap: 8px; }
  .brand-dot { width: 20px; height: 20px; border-radius: 50%; background: var(--pink); }
  .brand-name { font-family: "Open Sans", Arial, sans-serif; font-weight: 600; color: var(--pink); font-size: 21px; letter-spacing: 0.5px; }
  .front-cover .brand { position: absolute; left: 30px; top: 98px; }
  .claim {
    position: absolute; left: 44px; top: 146px; width: 230px;
    font-family: "Noto Serif", Georgia, serif; color: var(--pink);
    font-size: 23px; line-height: 1.25; font-weight: 400;
  }
  .claim strong { font-weight: 700; }

  /* Back cover */
  .back-cover { left: 640px; top: 50px; width: 520px; height: 368px; background: var(--black); }
  .contact-band {
    position: absolute; left: 0; top: 128px; width: 100%; height: 108px;
    background: var(--band); display: flex; align-items: center; padding-left: 56px; gap: 18px;
  }
  .contact-band .brand-name { font-size: 22px; }
  .contact-divider { width: 1px; height: 58px; background: var(--contact); opacity: 0.6; }
  .contact-list { list-style: none; font-size: 11px; line-height: 1.45; color: var(--contact); }

  /* Spreads */
  .spread { position: absolute; top: 520px; width: 560px; height: 340px; display: flex; box-shadow: 0 2px 6px rgba(0,0,0,0.18); }
  .spread-about { left: 30px; }
  .spread-products { left: 610px; }
  .spread .leaf { position: relative; width: 280px; height: 340px; background: var(--paper); overflow: hidden; }
  .spread .leaf + .leaf { border-left: 1px solid var(--fold); }

  .about-title {
    position: absolute; left: 22px; top: 58px;
    font-family: "Noto Serif", Georgia, serif; color: var(--pink); font-size: 16px; font-weight: 400;
  }
  .about-title::after { content: ""; display: block; width: 236px; height: 1px; background: var(--pink); margin-top: 4px; opacity: 0.6; }
  .about-copy { position: absolute; left: 22px; top: 94px; width: 236px; font-size: 7.5px; line-height: 1.55; color: var(--ink-soft); }
  .about-copy p + p { margin-top: 6px; }
  .about-copy .narrow { width: 122px; }
  .about-photo {
    position: absolute; right: 18px; top: 166px; width: 110px; height: 100px;
    background: linear-gradient(135deg, #d9cc56 0%, #8f9a3a 40%, #b35a63 75%, #d46a8d 100%);
  }

  .figure-art {
    position: absolute; left: 24px; top: 22px; width: 56px; height: 124px;
    background: linear-gradient(180deg, #ececec 0%, #3a3a3a 35%, #1f1f1f 100%);
  }
  .intro-box {
    position: absolute; left: 96px; top: 20px; width: 170px; height: 92px;
    background: var(--grey-box); color: #fff; font-size: 7.5px; line-height: 1.5; padding: 12px;
  }
  .intro-box p + p { margin-top: 6px; }

  .product-row { position: absolute; display: flex; gap: 8px; }
  .product { display: flex; flex-direction: column; align-items: center; gap: 5px; }
  .product-shot { width: 34px; background: #ddd; border-radius: 6px 6px 2px 2px; }
  .item-number {
    background: var(--pink); color: #fff; font-size: 6px; font-weight: 600;
    padding: 2px 5px; letter-spacing: 0.3px;
  }
  .row-lotion { left: 22px; top: 168px; gap: 6px; }
  .row-lotion .product-shot { height: 100px; background: linear-gradient(180deg, #c9c9c9 0%, #f4f4f4 25%, #e7d6e2 70%, #f2f2f2 100%); }

  .row-green { left: 14px; top: 66px; }
  .row-green .product-shot { height: 76px; background: linear-gradient(180deg, #1c5a2c 0%, #2f8f45 45%, #1d6a33 100%); }
  .row-mixed { left: 14px; top: 180px; }
  .row-mixed .product-shot { height: 90px; }
  .shot-violet { background: linear-gradient(180deg, #b9a9d2, #6d4f96); }
  .shot-peach { background: linear-gradient(180deg, #f2e1d6, #d8a98f); }
  .shot-pink { background: linear-gradient(180deg, #f5eef3, #e6bfd6); }
  .shot-blue { background: linear-gradient(180deg, #e6eaf7, #5d6fb8); }
</style>
</head>
<body>

  <section class="page front-cover" aria-label="Front cover">
    <div class="brand"><span class="brand-dot"></span><span class="brand-name">Lumvarex</span></div>
    <h1 class="claim">Europe’s leading<br>Afro-American<br><strong>Beauty Supplier</strong></h1>
    <div class="cover-photo" role="img" aria-label="Portrait photograph of a smiling woman in a grey top"></div>
  </section>

  <section class="page back-cover" aria-label="Back cover">
    <div class="contact-band">
      <div class="brand"><span class="brand-dot"></span><span class="brand-name">Lumvarex</span></div>
      <span class="contact-divider"></span>
      <ul class="contact-list">
        <li>Web: www.lumvarex.de</li>
        <li>Email: info@lumvarex.de</li>
        <li>Tel: +49 (0) 73 28 - 4 52 17</li>
        <li>Fax: +49 (0) 73 28 - 45 21 93</li>
      </ul>
    </div>
  </section>

  <section class="spread spread-about" aria-label="About spread">
    <div class="leaf">
      <h2 class="about-title">About Lumvarex of Beauty</h2>
      <div class="about-copy">
        <p>We are a family business and bring the best care products to shops all over Europe.</p>
        <p>We are sure you will find the right item for you and your store.</p>
        <p class="narrow">Our range covers hair care, skin care, styling and cosmetics from trusted brands. Fast delivery and fair prices make us a strong partner for salons and shops. Every order is packed with care and sent out within one working day from our own store in Germany.</p>
      </div>
      <div class="about-photo" role="img" aria-label="Collage of hair care product packs and styled hair"></div>
    </div>
    <div class="leaf">
      <div class="figure-art" role="img" aria-label="Illustration of a woman in a black dress"></div>
      <div class="intro-box">
        <p>Lumvarex of Beauty offers over 3,000 products for hair, skin and styling.</p>
        <p>We are sure you will find the right look for you.</p>
      </div>
      <div class="product-row row-lotion">
        <div class="product"><div class="product-shot" role="img" aria-label="Body lotion bottle"></div><span class="item-number">10411</span></div>
        <div class="product"><div class="product-shot" role="img" aria-label="Body lotion bottle"></div><span class="item-number">10412</span></div>
        <div class="product"><div class="product-shot" role="img" aria-label="Body lotion bottle"></div><span class="item-number">10413</span></div>
        <div class="product"><div class="product-shot" role="img" aria-label="Body lotion bottle"></div><span class="item-number">10414</span></div>
        <div class="product"><div class="product-shot" role="img" aria-label="Body lotion bottle"></div><span class="item-number">10415</span></div>
        <div class="product"><div class="product-shot" role="img" aria-label="Body lotion bottle"></div><span class="item-number">10416</span></div>
      </div>
    </div>
  </section>

  <section class="spread spread-products" aria-label="Product spread">
    <div class="leaf">
      <div class="product-row row-green">
        <div class="product"><div class="product-shot" role="img" aria-label="Green bottle"></div><span class="item-number">20101</span></div>
        <div class="product"><div class="product-shot" role="img" aria-label="Green bottle"></div><span class="item-number">20102</span></div>
        <div class="product"><div class="product-shot" role="img" aria-label="Green bottle"></div><span class="item-number">20103</span></div>
        <div class="product"><div class="product-shot" role="img" aria-label="Green bottle"></div><span class="item-number">20104</span></div>
        <div class="product"><div class="product-shot" role="img" aria-label="Green bottle"></div><span class="item-number">20105</span></div>
        <div class="product"><div class="product-shot" role="img" aria-label="Green bottle"></div><span class="item-number">20106</span></div>
      </div>
      <div class="product-row row-mixed">
        <div class="product"><div class="product-shot shot-violet" role="img" aria-label="Violet product box"></div><span class="item-number">30201</span></div>
        <div class="product"><div class="product-shot shot-peach" role="img" aria-label="Cream bottle"></div><span class="item-number">30202</span></div>
        <div class="product"><div class="product-shot shot-pink" role="img" aria-label="Pink spray bottle"></div><span class="item-number">30203</span></div>
        <div class="product"><div class="product-shot shot-blue" role="img" aria-label="Blue cream jar"></div><span class="item-number">30204</span></div>
        <div class="product"><div class="product-shot shot-blue" role="img" aria-label="Blue cream jar"></div><span class="item-number">30205</span></div>
        <div class="product"><div class="product-shot shot-blue" role="img" aria-label="Blue cream box"></div><span class="item-number">30206</span></div>
      </div>
    </div>
    <div class="leaf" aria-label="Blank page"></div>
  </section>

</body>
</html>
```